Real Estate | Property Management Website Design

We are working with a Real Estate company in California. They provide Property Management Services and Real Estate Services.

PLEASE NOT: make sure the site covers real estate and property management).

A few websites for inspiration:
https://pinebrookleases.com
https://www.varmolhomeadvisors.com
https://marisotelvy.com
https://tobenhalvrick.com
https://thecalvenparty.com
https://ronaquistmoor.com
https://zvask.com

Thank you for taking the time to consider designing a website for us. We are web developers based in Stockton, CA, USA. Most of our projects go through the same process. Understanding this process may help you win a project with us. We custom-code all of our websites in-house. We don’t have any requirements as to what tools you use for your design, but we ask that you follow these guidelines.

IMAGES:
If you use any images or icons in the design, we ask that you have a link to the asset so we can purchase the image/icon. Most of the designs we submit do not have the customer’s images on them unless they have some great images. Be creative; show us the feeling you are trying to portray with your image choices. Use any royalty-free site you choose. We subscribe to Plimora and mainly use their images, but we can purchase images outside of Plimora. PLEASE NOTE: we will not submit designs to clients with watermarks on the images.

FONTS:
We ask that you identify the fonts you’re using in the design. This can be done in a message if you want. We typically use Quendle Fonts and Plimora Fonts.

CONTENT:
We're always open to different content and ideas. We often submit designs with stock images so the client can see our vision. We typically take pictures after the website launch to use their images with our vision. Lorem Ipsum is fine for paragraphs, but we ask that you make the Headers with correct English. We want to be able to show the vision and identify the sections of the website.

INSPIRATION:
We typically add a couple of links in the brief of websites we like to help you get started in your design.

REVISIONS:
We do not often ask for revisions of the designs unless we see something in the design that may not appeal to the client. If there are slight changes that we want to make, we do that in the development process.

FEEDBACK:
We rarely give feedback on designs during the design process. We are working on many website projects and do not have the time to provide feedback. We usually respond if your request is well thought out and asks specific questions, but a note asking “feedback, please” usually goes unanswered.

```html
<!DOCTYPE html>
<html lang="en">
<head>
<meta charset="utf-8">
<title>Harborline Properties</title>
<link rel="stylesheet" href="https://fonts.googleapis.com/css2?family=Trirong:wght@300;400&family=Poppins:wght@300;400;500;600&display=swap">
<style>
:root{
  --orange:#f47b2a;
  --ink:#3f3f3f;
  --muted:#666;
  --sand:#f1eee9;
  --sand2:#eceae6;
  --dark:#363b40;
  --darker:#24282c;
  --field:#e6e6e6;
  --white:#fff;
}
*{margin:0;padding:0;box-sizing:border-box}
html,body{width:1200px;height:3769px;overflow:hidden}
body{font-family:'Poppins',sans-serif;color:var(--ink);background:var(--white);position:relative}
.abs{position:absolute}
.serif{font-family:'Trirong',serif;font-weight:300}
section,header,footer{position:absolute;left:0;width:1200px}
.topbar{top:0;height:32px;background:#ececec;font-size:10px;color:var(--orange)}
.topbar span{position:absolute;top:10px;display:flex;align-items:center;gap:8px}
.navbar{top:32px;height:41px;background:#f6f6f6;border-bottom:1px solid #e2e2e2}
.brand{display:flex;align-items:center;gap:8px;color:var(--orange);font-weight:600;font-size:15px;letter-spacing:.5px}
.brand i{display:block;width:22px;height:22px;background:var(--orange)}
.nav-links{position:absolute;left:485px;top:13px;display:flex;gap:24px;font-size:10.5px;color:#333}
.btn-outline{position:absolute;left:831px;top:5px;width:139px;height:29px;border:1.5px solid var(--orange);border-radius:15px;color:var(--orange);font-size:10.5px;display:flex;align-items:center;justify-content:center}
.hero{top:73px;height:496px;background:linear-gradient(180deg,#5fa5cf,#86c0dc)}
.hero-photo{position:absolute;left:490px;top:40px;width:710px;height:456px;background:linear-gradient(135deg,#e9eef2,#9fb3c2 60%,#6e8798);clip-path:polygon(40% 100%,55% 30%,90% 0,100% 20%,100% 100%)}
.hero h1{position:absolute;left:231px;top:172px;font-size:27px;color:#fff}
.hero p{position:absolute;left:231px;top:222px;font-size:14px;line-height:22px;color:#fff}
.btn{background:var(--orange);color:#fff;font-size:12px;font-weight:500;display:flex;align-items:center;justify-content:center;letter-spacing:.5px}
.hero .btn{position:absolute;left:231px;top:290px;width:150px;height:30px}
.view-bar{position:absolute;left:778px;top:465px;width:422px;height:31px;background:rgba(232,120,55,.85);color:#fff;font-size:13px;padding-left:20px;display:flex;align-items:center;gap:8px}
.about{top:569px;height:496px}
.panel{position:absolute;box-shadow:6px 8px 16px rgba(0,0,0,.18)}
.about h2{position:absolute;left:581px;top:92px;font-size:25px}
.about .lead{position:absolute;left:581px;top:146px;width:360px;font-size:10px;font-weight:600;line-height:22px}
.about .body{position:absolute;left:581px;top:213px;width:370px;font-size:10px;line-height:22.5px;color:var(--muted)}
.link{position:absolute;left:581px;top:355px;color:var(--orange);font-size:12px;display:flex;gap:8px;align-items:center}
.services{top:1065px;height:413px;background:var(--sand)}
.section-title{position:absolute;left:0;width:1200px;text-align:center;font-size:25px;color:#444}
.service{position:absolute;width:170px;text-align:center}
.service svg{display:block;margin:0 auto}
.service h3{font-family:'Trirong',serif;font-weight:300;font-size:15px;margin-top:14px;color:#555}
.service p{font-size:10px;line-height:15px;color:var(--muted);margin-top:12px}
.listings{top:1478px;height:699px}
.listings .intro{position:absolute;left:380px;top:128px;width:440px;text-align:center;font-size:11px;line-height:22.5px;color:#444}
.featured{position:absolute;left:231px;top:324px;font-size:16px;color:#555}
.arrows{position:absolute;left:922px;top:326px;display:flex;gap:22px}
.card{position:absolute;top:364px;width:239px}
.card .photo{height:157px}
.card h4{font-size:12.5px;font-weight:400;margin-top:12px;color:#333}
.card h4 span{color:#777}
.card .loc{font-size:9.5px;color:#444;margin-top:3px}
.card .price{font-size:12px;color:var(--orange);margin-top:6px}
.testimonials{top:2177px;height:425px;background:linear-gradient(180deg,var(--sand2),#f4f3f1)}
.quote{position:absolute;left:400px;top:170px;width:400px;text-align:center;font-style:italic;font-size:17px;line-height:19.5px;color:#666;font-weight:300}
.avatar{position:absolute;left:575px;top:302px;width:50px;height:50px;border-radius:50%;background:linear-gradient(135deg,#d8d2cc,#8c7f76);border:3px solid #fff}
.person{position:absolute;left:0;top:358px;width:1200px;text-align:center;font-size:11.5px;color:#333}
.partners{top:2602px;height:123px;background:linear-gradient(180deg,#9a9da0,#6d7276)}
.partners h5{position:absolute;left:0;width:1200px;top:25px;text-align:center;font-family:'Trirong',serif;font-weight:300;font-size:16px;color:#fff}
.badge{position:absolute;top:64px;height:24px;border-radius:12px;background:rgba(255,255,255,.55)}
.work{top:2725px;height:329px}
.work p{position:absolute;left:390px;top:142px;width:420px;text-align:center;font-family:'Trirong',serif;font-size:11px;line-height:19px;color:#555}
.work .btn{position:absolute;left:525px;top:211px;width:150px;height:30px}
.chat{top:3054px;height:429px;background:linear-gradient(135deg,#b9b2a4,#8e9478 40%,#c7c0b3 70%,#7a8466)}
.chat-card{position:absolute;left:268px;top:57px;width:664px;height:313px;background:#fff}
.chat-card h2{position:absolute;left:73px;top:32px;font-size:22px;color:#333}
.chat-card p{position:absolute;left:73px;top:78px;width:240px;font-family:'Trirong',serif;font-size:10.5px;line-height:19px;color:#555}
.hotline{position:absolute;left:73px;top:158px;font-family:'Trirong',serif;font-size:10.5px;line-height:19px;color:#444;display:flex;gap:10px}
.field{position:absolute;left:366px;width:222px;background:var(--field);font-size:9.5px;color:#999;padding:6px 12px}
.send{position:absolute;left:366px;top:262px;width:222px;height:26px;font-size:9.5px;font-weight:600}
footer{top:3483px;height:286px;background:var(--dark);color:#fff}
.f-col{position:absolute;top:62px}
.f-col h6{font-family:'Trirong',serif;font-weight:300;font-size:16px;color:var(--orange);margin-bottom:14px}
.f-col li{list-style:none;font-size:10.5px;line-height:18.5px}
.f-contact{position:absolute;left:234px;top:97px;font-size:10.5px;line-height:18.5px;list-style:none}
.socials{display:flex;gap:10px}
.socials i{display:block;width:26px;height:26px;border:1.5px solid #fff;border-radius:50%}
.copy{position:absolute;left:0;top:260px;width:1200px;height:26px;background:var(--darker);text-align:center;font-size:10.5px;line-height:26px}
</style>
</head>
<body>

<header class="topbar">
  <span style="left:231px"><svg width="13" height="13" viewBox="0 0 24 24"><path d="M12 2a7 7 0 0 0-7 7c0 5 7 13 7 13s7-8 7-13a7 7 0 0 0-7-7z" fill="var(--orange)"/><circle cx="12" cy="9" r="2.5" fill="#fff"/></svg>E 22nd Avenue, Fresno, CA 93702</span>
  <span style="left:634px"><svg width="13" height="13" viewBox="0 0 24 24"><circle cx="12" cy="12" r="12" fill="var(--orange)"/><path d="M8 6l2 3-1 2a7 7 0 0 0 4 4l2-1 3 2-1 2c-6 0-11-5-11-11z" fill="#fff"/></svg>(245) 555-0140</span>
  <span style="left:783px"><svg width="14" height="13" viewBox="0 0 24 24"><circle cx="12" cy="12" r="11" fill="none" stroke="var(--orange)" stroke-width="2"/><rect x="6" y="8" width="12" height="8" fill="none" stroke="var(--orange)" stroke-width="1.6"/><path d="M6 8l6 5 6-5" fill="none" stroke="var(--orange)" stroke-width="1.6"/></svg>info@harborlineproperties.com</span>
</header>

<header class="navbar">
  <div class="brand abs" style="left:231px;top:9px"><i></i>HARBORLINE</div>
  <nav class="nav-links"><span>Services ▾</span><span>Property Search</span><span>Press</span><span>About</span><span>Contact</span></nav>
  <div class="btn-outline">Schedule A Call</div>
</header>

<section class="hero">
  <div class="hero-photo" role="img" aria-label="Modern high-rise apartment building with balconies against a blue sky"></div>
  <h1 class="serif">Welcome to Harborline Properties</h1>
  <p class="serif">Your Trusted California Real Estate<br>and Property Management Experts</p>
  <div class="btn">CALL NOW</div>
  <div class="view-bar">View Our Properties
    <svg width="9" height="12" viewBox="0 0 9 12"><path d="M2 1l5 5-5 5" stroke="#fff" stroke-width="2.2" fill="none"/></svg></div>
</section>

<section class="about">
  <svg class="panel" style="left:0;top:0;width:560px;height:496px;box-shadow:none" viewBox="0 0 560 496">
    <defs>
      <linearGradient id="villa" x1="0" y1="0" x2="0" y2="1"><stop offset="0" stop-color="#8cb6d6"/><stop offset=".55" stop-color="#d9d6cf"/><stop offset="1" stop-color="#46b3c8"/></linearGradient>
      <linearGradient id="garden" x1="0" y1="0" x2="1" y2="1"><stop offset="0" stop-color="#a8cbe4"/><stop offset=".5" stop-color="#e8e6e1"/><stop offset="1" stop-color="#3f6a35"/></linearGradient>
    </defs>
    <polygon points="138,146 230,141 230,405 138,421" fill="url(#garden)" role="img" aria-label="White modern house exterior with walkway"/>
    <polygon points="241,-54 398,-23 398,436 241,397" fill="url(#villa)" role="img" aria-label="Modern villa with glass walls and pool"/>
    <polygon points="410,31 531,59 531,407 410,407" fill="url(#garden)" role="img" aria-label="Pool terrace with tropical plants"/>
  </svg>
  <h2 class="serif">ABOUT US</h2>
  <p class="lead">Discover your dream home or maximize the value of your property with Harborline Properties.</p>
  <p class="body">As a premier real estate and property management firm in California, we offer a comprehensive range of services tailored to meet your unique needs. Whether you're buying, selling, renting, or seeking professional property management solutions, we have the expertise and dedication to deliver exceptional results.</p>
  <div class="link">Learn More <svg width="7" height="11" viewBox="0 0 7 11"><path d="M1 1l4.5 4.5L1 10" stroke="var(--orange)" stroke-width="1.8" fill="none"/></svg></div>
</section>

<section class="services">
  <h2 class="section-title serif" style="top:62px">WHAT WE DO</h2>
  <div class="service" style="left:293px;top:147px">
    <svg width="82" height="74" viewBox="0 0 82 74" fill="none" stroke="var(--orange)" stroke-width="2.5"><rect x="4" y="16" width="18" height="54"/><rect x="22" y="6" width="20" height="64"/><rect x="42" y="14" width="16" height="56"/><path d="M58 40h12v30H58M0 70h82"/><circle cx="74" cy="52" r="5"/><path d="M9 24h8M9 34h8M9 44h8M27 16h10M27 28h10M27 40h10M47 24h6M47 34h6"/></svg>
    <h3>Sales &amp; Purchases</h3>
    <p>Lorem ipsum dolor sit amet, consectetur adipiscing elit, sed do eiusmod tempor incididunt ut labore.</p>
  </div>
  <div class="service" style="left:514px;top:140px">
    <svg width="82" height="82" viewBox="0 0 82 82" fill="none" stroke="var(--orange)" stroke-width="2.5"><path d="M4 34L41 6l37 28"/><path d="M12 28v48h58V28"/><circle cx="41" cy="46" r="14"/><path d="M45 40h-6a3 3 0 0 0 0 6h4a3 3 0 0 1 0 6h-6M41 36v4M41 52v4"/><circle cx="66" cy="52" r="7"/><path d="M52 66h14"/></svg>
    <h3>Lease &amp; Rentals</h3>
    <p>Consectetur adipiscing elit, sed do eiusmod tempor incididunt ut labore et dolore magna.</p>
  </div>
  <div class="service" style="left:740px;top:143px">
    <svg width="80" height="80" viewBox="0 0 80 80" fill="none" stroke="var(--orange)" stroke-width="2.5"><circle cx="40" cy="40" r="15"/><path d="M33 43v-6l7-5 7 5v6z"/><path d="M40 25V12M40 55v13M25 40H12M55 40h13M29 29l-8-8M51 51l8 8M51 29l8-8M29 51l-8 8"/><circle cx="40" cy="8" r="4"/><circle cx="40" cy="72" r="4"/><circle cx="8" cy="40" r="4"/><circle cx="72" cy="40" r="4"/><circle cx="18" cy="18" r="4"/><circle cx="62" cy="62" r="4"/><circle cx="62" cy="18" r="4"/><circle cx="18" cy="62" r="4"/></svg>
    <h3>Management</h3>
    <p>Sed do eiusmod tempor incididunt ut labore et dolore magna ipsum dolor amet.</p>
  </div>
</section>

<section class="listings">
  <h2 class="section-title serif" style="top:60px">EXPLORE OUR EXTENSIVE PROPERTY LISTINGS</h2>
  <p class="intro">Browse through our diverse selection of residential and commercial properties, meticulously curated to cater to every taste and budget. From stunning beachfront estates to urban condominiums and office spaces, we have the perfect property waiting for you. Our advanced search tools make it easy to find your ideal home or investment opportunity.</p>
  <div class="featured serif">Featured Properties</div>
  <div class="arrows">
    <svg width="8" height="13" viewBox="0 0 8 13"><path d="M7 1L2 6.5 7 12" stroke="#f6c3a0" stroke-width="2" fill="none"/></svg>
    <svg width="8" height="13" viewBox="0 0 8 13"><path d="M1 1l5 5.5L1 12" stroke="var(--orange)" stroke-width="2" fill="none"/></svg>
  </div>
  <div class="card" style="left:231px">
    <div class="photo" role="img" aria-label="White modern villa with swimming pool" style="background:linear-gradient(180deg,#d8e6f0,#f2f2f0 55%,#4fc0d8)"></div>
    <h4>17 Cedar Bluff Drive <span>#D20001</span></h4>
    <div class="loc">Lake Mercer, San Francisco, CA</div>
    <div class="price">$ 3,240,000</div>
  </div>
  <div class="card" style="left:481px">
    <div class="photo" role="img" aria-label="Glass-walled house with pool and garden" style="background:linear-gradient(180deg,#cdd9cf,#c8bda9 55%,#3d8f9a)"></div>
    <h4>46 Willow Crest Street <span>#D34001</span></h4>
    <div class="loc">Fresno, CA</div>
    <div class="price">$ 2,640,000</div>
  </div>
  <div class="card" style="left:730px">
    <div class="photo" role="img" aria-label="Timber lodge home at dusk with reflecting pool" style="background:linear-gradient(180deg,#4f6e88,#7a5236 50%,#3c6f8a)"></div>
    <h4>9 Sorrel Ridge Drive <span>#D12004</span></h4>
    <div class="loc">San Diego, CA</div>
    <div class="price">$ 6,240,000</div>
  </div>
</section>

<section class="testimonials">
  <h2 class="section-title serif" style="top:68px">WHAT OUR CUSTOMERS SAY</h2>
  <svg class="abs" style="left:266px;top:180px" width="24" height="46" viewBox="0 0 24 46"><path d="M22 2L3 23l19 21" stroke="#999" stroke-width="2" fill="none"/></svg>
  <svg class="abs" style="left:910px;top:180px" width="24" height="46" viewBox="0 0 24 46"><path d="M2 2l19 21L2 44" stroke="#999" stroke-width="2" fill="none"/></svg>
  <p class="quote">Lorem ipsum dolor sit amet, con sectetur adipiscing elit, sed do eiusmod tempor incididunt ut labore et dolore magna aliqua. Quis ipsum suspendisse ultrices gravida.</p>
  <div class="avatar" role="img" aria-label="Portrait of the client"></div>
  <div class="person">Mara Ellison</div>
</section>

<section class="partners" role="img" aria-label="City bridge skyline backdrop">
  <h5>OUR PARTNERS</h5>
  <div class="badge" style="left:232px;width:108px"></div>
  <div class="badge" style="left:438px;width:102px"></div>
  <div class="badge" style="left:628px;width:128px"></div>
  <div class="badge" style="left:841px;width:128px"></div>
</section>

<section class="work">
  <h2 class="section-title serif" style="top:86px">WORK WITH US</h2>
  <p>Start your real estate journey with Harborline Properties. Contact our team of experts to schedule a consultation. Your California dream is just a step away.</p>
  <div class="btn">CALL NOW</div>
</section>

<section class="chat" role="img" aria-label="Aerial view of a residential neighbourhood with pools and trees">
  <div class="chat-card">
    <h2 class="serif">LET'S HAVE A CHAT!</h2>
    <p>Get in touch with us for any questions or inquiries and we'll get back to you within 24 hours. Send us a message or call us directly.</p>
    <div class="hotline"><span>Hotline •</span><span>(245) 555-0140<br>• (245) 555-0141<br>• (245) 555-0142</span></div>
    <div class="field" style="top:31px;height:25px">First Name</div>
    <div class="field" style="top:72px;height:25px">Email Address</div>
    <div class="field" style="top:113px;height:25px">Phone Number</div>
    <div class="field" style="top:152px;height:95px">Your Message</div>
    <div class="btn send">SEND</div>
  </div>
</section>

<footer>
  <div class="brand abs" style="left:230px;top:45px"><i></i>HARBORLINE</div>
  <ul class="f-contact">
    <li>• 4100 E Linden Street,</li>
    <li>&nbsp;&nbsp;Fresno, CA 93702</li>
    <li>• info@harborlineproperties.com</li>
    <li>• (245) 555-0140</li>
  </ul>
  <div class="f-col" style="left:468px"><h6>Quick Links</h6><ul><li>• Services</li><li>• Property Search</li><li>• Press</li><li>• About</li><li>• Contact</li></ul></div>
  <div class="f-col" style="left:634px"><h6>Resources</h6><ul><li>• Owner Resources</li><li>• Customer Resources</li><li>• FAQ</li><li>• Legal</li></ul></div>
  <div class="f-col" style="left:836px"><h6>Social Media</h6><div class="socials"><i></i><i></i><i></i><i></i></div></div>
  <div class="copy">www.harborlineproperties.com</div>
</footer>

</body>
</html>
```